Startup Drone Platform Company business card

We are needing a business card design for our employees. We are a startup drone platform. We are looking for a business card that has our logo on one side, with the employee/company details on the opposite side. We are looking for something that is very eye catching, modern, and bold.

Target Market(s)

This will target both drone pilots and drone businesses, along with all the industries that could utilize drone services (aerial video, aerial photos, inspections, 3d mapping, etc).

Industry/Entity Type

Business

```html
<!DOCTYPE html>
<html lang="en">
<head>
<meta charset="utf-8">
<title>Skylane Aerial – Business Card</title>
<link href="https://fonts.googleapis.com/css2?family=Questrial&family=Montserrat:wght@600&display=swap" rel="stylesheet">
<style>
  :root {
    --bg: #1c1c1c;
    --card-dark: #2b2b2b;
    --card-dark-deep: #1f1f1f;
    --paper: #f4f4f4;
    --teal: #13c4cf;
    --ink: #1a1a1a;
    --muted: #8a8a8a;
    --light-text: #e6e6e6;
  }
  * { box-sizing: border-box; margin: 0; padding: 0; }
  html, body { width: 1200px; height: 900px; overflow: hidden; }
  body {
    background: var(--bg);
    font-family: "Questrial", sans-serif;
    position: relative;
  }
  .card {
    position: absolute;
    left: 285px;
    width: 630px;
    height: 360px;
    overflow: hidden;
    box-shadow: 0 10px 30px rgba(0,0,0,0.5);
  }
  .card--back { top: 50px; background: linear-gradient(160deg, #353535, var(--card-dark-deep)); }
  .card--front { top: 490px; background: var(--card-dark); }

  .wordmark {
    display: flex;
    align-items: center;
    gap: 16px;
    font-family: "Questrial", sans-serif;
    letter-spacing: 0.45em;
    text-transform: uppercase;
    white-space: nowrap;
  }
  .wordmark__dot {
    width: 14px; height: 14px; border-radius: 50%;
    background: var(--teal); flex: none;
  }

  /* back */
  .card--back .wordmark {
    position: absolute; left: 0; right: 0; top: 125px;
    justify-content: center;
    color: var(--light-text);
    font-size: 30px;
  }
  .back__url {
    position: absolute; left: 0; right: 0; top: 205px;
    text-align: center; color: #cfcfcf; font-size: 15px; letter-spacing: 0.03em;
  }
  .back__band { position: absolute; left: 0; right: 0; bottom: 14px; height: 26px; background: var(--teal); }

  /* front */
  .front__paper {
    position: absolute; left: 0; top: 0; right: 0; height: 190px;
    background: var(--paper);
  }
  .front__notch {
    position: absolute; left: 238px; top: 189px;
    width: 0; height: 0;
    border-left: 10px solid transparent;
    border-right: 10px solid transparent;
    border-top: 10px solid var(--paper);
  }
  .card--front .wordmark {
    position: absolute; right: 30px; top: 58px;
    color: var(--ink); font-size: 22px;
  }
  .person { position: absolute; left: 44px; top: 112px; }
  .person__name {
    font-family: "Montserrat", sans-serif; font-weight: 600;
    color: var(--teal); font-size: 24px; letter-spacing: 0.02em; text-transform: uppercase;
  }
  .person__role { color: var(--muted); font-size: 17px; margin-top: 2px; }

  .contacts { position: absolute; left: 262px; top: 212px; list-style: none; }
  .contacts li {
    display: flex; align-items: center; gap: 12px;
    color: var(--light-text); font-size: 15px; height: 21px;
  }
  .contacts svg { width: 16px; height: 16px; flex: none; }

  .address {
    position: absolute; right: 30px; top: 206px;
    text-align: right; color: var(--light-text); font-size: 15px; line-height: 1.4;
    font-style: normal;
  }
  .front__band { position: absolute; left: 0; right: 0; top: 308px; height: 30px; background: var(--teal); }
</style>
</head>
<body>

<section class="card card--back" aria-label="Card back">
  <div class="wordmark"><span>Skylane Aerial</span><span class="wordmark__dot"></span></div>
  <p class="back__url">www.skylaneaerial.com</p>
  <div class="back__band"></div>
</section>

<section class="card card--front" aria-label="Card front">
  <div class="front__paper"></div>
  <div class="front__notch"></div>
  <div class="wordmark"><span>Skylane Aerial</span><span class="wordmark__dot"></span></div>
  <div class="person">
    <p class="person__name">Morgan Ellery</p>
    <p class="person__role">Office Manager</p>
  </div>
  <address class="address">48 Harbor Lane<br>Suite 12<br>Fairview MA 01234</address>
  <ul class="contacts">
    <li>
      <svg viewBox="0 0 16 16"><rect width="16" height="16" rx="3" fill="#13c4cf"/><rect x="5" y="3" width="6" height="10" rx="1" fill="none" stroke="#fff" stroke-width="1.3"/></svg>
      555.014.2910
    </li>
    <li>
      <svg viewBox="0 0 16 16"><rect width="16" height="16" rx="3" fill="#13c4cf"/><path d="M5 3.5l2 2-1 1.2c.6 1.3 1.6 2.3 2.8 2.8l1.2-1 2 2-1.3 1.6C7.4 12 4 8.6 3.9 5z" fill="#fff"/></svg>
      555.014.2971
    </li>
    <li>
      <svg viewBox="0 0 16 16"><rect width="16" height="16" rx="3" fill="#13c4cf"/><rect x="3.5" y="4.5" width="9" height="7" fill="none" stroke="#fff" stroke-width="1.2"/><path d="M3.5 4.5L8 8.5l4.5-4" fill="none" stroke="#fff" stroke-width="1.2"/></svg>
      info@skylaneaerial.com
    </li>
    <li>
      <svg viewBox="0 0 16 16"><rect width="16" height="16" rx="3" fill="#13c4cf"/><circle cx="8" cy="8" r="4.5" fill="none" stroke="#fff" stroke-width="1.1"/><ellipse cx="8" cy="8" rx="2" ry="4.5" fill="none" stroke="#fff" stroke-width="1"/><path d="M3.5 8h9" stroke="#fff" stroke-width="1"/></svg>
      www.skylaneaerial.com
    </li>
  </ul>
  <div class="front__band"></div>
</section>

</body>
</html>
```